Dental clinic brochure design (Z fold)

We need a new brochure design made for our dental clinic - Brindlemoor Dental Surgery. One side is in English, the other is in Vietnamese - all text and translations provided in brochure sample with further instructions in word doc. We require a brochure design in a Z fold to convey a family friendly dental clinic, incorporating our logo colour into the theme and designers choice on complimentary colours. Additional high quality images are provided for use if required or free to use own images.

Colors
33b8a4
00a990
86cfc6

Requirements
Must have
• Easy to read font, flows from text to pictures and page to page
• At least 2 dental images

```html
<!DOCTYPE html>
<html lang="en">
<head>
<meta charset="utf-8">
<title>Brindlemoor Dental Surgery – Z-fold brochure</title>
<link rel="stylesheet" href="https://fonts.googleapis.com/css2?family=Raleway:wght@300;400;500;600;700;800&display=swap">
<style>
  :root {
    --teal: #33b8a4;
    --teal-deep: #00a990;
    --teal-soft: #86cfc6;
    --ice: #cfe9f1;
    --slate: #5e5f61;
    --ink: #2b2b2b;
    --grey-text: #6b6c6e;
    --page: #e4e5e6;
    --paper: #ffffff;
  }
  * { box-sizing: border-box; margin: 0; padding: 0; }
  html, body { width: 1200px; height: 2590px; overflow: hidden; }
  body {
    background: var(--page);
    font-family: "Raleway", Arial, sans-serif;
    position: relative;
  }
  .sheet {
    position: absolute;
    left: 90px;
    width: 1020px;
    height: 794px;
    background: var(--paper);
    box-shadow: 0 6px 16px rgba(0,0,0,.25);
    overflow: hidden;
  }
  .sheet--outside { top: 451px; }
  .sheet--inside { top: 1345px; }
  .sheet__bg { position: absolute; inset: 0; }
  .block { position: absolute; }
  .heading {
    font-weight: 800;
    font-size: 23px;
    line-height: 1.28;
    text-transform: uppercase;
    letter-spacing: .3px;
  }
  .heading--teal { color: var(--teal); }
  .heading--white { color: #fff; }
  .body-copy { font-size: 15px; line-height: 1.45; color: var(--grey-text); font-weight: 500; }
  .body-copy p + p { margin-top: 18px; }
  .body-copy--dark { color: var(--ink); font-weight: 600; }
  .body-copy--white { color: #fff; font-weight: 600; text-align: center; }
  .accent { color: var(--teal); }

  .note-bar {
    left: 0; top: 622px; width: 337px; height: 86px;
    background: var(--slate);
    color: #fff; font-size: 17px; font-weight: 500;
    display: flex; align-items: center; padding-left: 42px;
  }
  .wordmark {
    left: 675px; top: 372px; width: 345px;
    display: flex; flex-direction: column; align-items: center; gap: 12px;
  }
  .wordmark__dot { width: 30px; height: 30px; border-radius: 50%; background: var(--teal); }
  .wordmark__name {
    font-size: 19px; font-weight: 500; letter-spacing: 3px;
    color: var(--slate); text-transform: uppercase; text-align: center; line-height: 1.35;
  }
  .title-box {
    left: 705px; top: 497px; width: 315px; height: 178px;
    background: var(--slate); color: #fff;
    padding: 18px 20px 0 24px; text-transform: uppercase; line-height: 1;
  }
  .title-box__line1 { font-size: 33px; font-weight: 800; letter-spacing: .2px; }
  .title-box__line2 { font-size: 54px; font-weight: 300; margin-top: 4px; }
  .title-box__line3 { font-size: 50px; font-weight: 500; }
  .contact-front {
    left: 675px; top: 690px; width: 345px; text-align: center;
    color: var(--teal); font-size: 19px; line-height: 1.3; font-weight: 500;
  }
  .contact-front strong { font-weight: 800; font-size: 21px; }

  .scheme-box {
    left: 43px; top: 345px; width: 270px; height: 384px;
    background: var(--slate); color: #fff; padding: 30px 20px 0 20px;
  }
  .scheme-box .heading { font-size: 21px; }
  .scheme-box .text { font-size: 14px; line-height: 1.4; font-weight: 600; margin-top: 18px; }
  .scheme-box .call { margin-top: 28px; font-size: 24px; font-weight: 600; line-height: 1.15; }
  .scheme-box .call strong { font-size: 34px; font-weight: 800; display: block; }

  .address-bar {
    left: 361px; top: 673px; width: 300px; height: 82px;
    background: var(--slate); color: #fff; text-align: center;
    font-size: 13px; font-weight: 600; line-height: 1.35; padding-top: 8px;
  }
  .providers { left: 715px; top: 234px; width: 300px; }
  .provider + .provider { margin-top: 9px; }
  .provider__name { color: var(--teal); font-size: 19px; font-weight: 700; text-transform: uppercase; line-height: 1.1; }
  .provider__creds { color: var(--grey-text); font-size: 11.5px; font-weight: 600; line-height: 1.3; }
  .photo, .map { position: absolute; }
</style>
</head>
<body>

<!-- Outside: Vietnamese panels -->
<section class="sheet sheet--outside" lang="vi">
  <svg class="sheet__bg" width="1020" height="794" viewBox="0 0 1020 794">
    <defs>
      <linearGradient id="kids-tone" x1="0" y1="0" x2="0" y2="1">
        <stop offset="0" stop-color="#e9d8c8"/><stop offset="1" stop-color="#c9b9c8"/>
      </linearGradient>
      <linearGradient id="babies-tone" x1="0" y1="0" x2="1" y2="0">
        <stop offset="0" stop-color="#f1e1d3"/><stop offset="1" stop-color="#d9b9a0"/>
      </linearGradient>
      <linearGradient id="smile-tone" x1="0" y1="0" x2="1" y2="1">
        <stop offset="0" stop-color="#f4e8e4"/><stop offset="1" stop-color="#e2c6c0"/>
      </linearGradient>
    </defs>
    <rect x="337" y="0" width="338" height="794" fill="var(--teal)"/>
    <polygon points="200,0 337,0 337,165" fill="var(--teal)"/>
    <polygon points="250,794 337,794 337,700" fill="var(--teal)"/>
    <polygon points="506,199 675,370 506,541 337,370" fill="#fff"/>
    <polygon points="330,330 390,390 330,450 270,390" fill="var(--ice)" opacity=".85"/>
    <polygon points="506,240 636,370 506,500 376,370" fill="url(#kids-tone)" role="img" aria-label="Photo: row of smiling children"/>
    <rect x="0" y="414" width="337" height="208" fill="url(#babies-tone)" role="img" aria-label="Photo: two toddlers brushing their teeth"/>
    <polygon points="675,0 1020,0 1020,230 675,320" fill="url(#smile-tone)" role="img" aria-label="Photo: close-up smile holding a clear aligner"/>
  </svg>

  <div class="block" style="left:55px; top:92px; width:260px;">
    <h2 class="heading heading--teal">Special<br>Promotions</h2>
    <div class="body-copy" style="margin-top:26px;">
      <p>Khám răng, chụp hình x-ray và clean răng chỉ nhận bảo hiểm**</p>
      <p>Giá Đặc biệt 1 Bộ Tẩy Trắng Răng $199 thông thường là $395</p>
    </div>
  </div>
  <div class="block note-bar">**Gọi nhân viên để biết thêm</div>

  <div class="block" style="left:337px; top:83px; width:338px; text-align:center;">
    <h2 class="heading heading--white">Child Dental<br>Benefits Scheme</h2>
  </div>
  <div class="block body-copy body-copy--white" style="left:370px; top:612px; width:272px;">
    <p>Chúng tôi nhận chương trình Medicare $1000 mỗi 2 năm cho thiếu nhi tuổi từ 2 đến 17.</p>
    <p>Xin vui lòng liên lạc văn phòng số đt (03) 9400 2186.</p>
  </div>

  <div class="block wordmark">
    <span class="wordmark__dot"></span>
    <span class="wordmark__name">Brindlemoor Dental Surgery</span>
  </div>
  <div class="block title-box">
    <div class="title-box__line1">Brindlemoor</div>
    <div class="title-box__line2">Dental</div>
    <div class="title-box__line3">Surgery</div>
  </div>
  <div class="block contact-front">
    <strong>Phone: (03) 9400 2186</strong><br>
    48 Alderbrook Road,<br>Westvale, VIC 3999
  </div>
</section>

<!-- Inside: English panels -->
<section class="sheet sheet--inside" lang="en">
  <svg class="sheet__bg" width="1020" height="794" viewBox="0 0 1020 794">
    <defs>
      <linearGradient id="group-tone" x1="0" y1="0" x2="1" y2="1">
        <stop offset="0" stop-color="#f0dccb"/><stop offset="1" stop-color="#d8c27e"/>
      </linearGradient>
      <linearGradient id="girl-tone" x1="0" y1="0" x2="1" y2="0">
        <stop offset="0" stop-color="#d7c4b4"/><stop offset="1" stop-color="#efe3d8"/>
      </linearGradient>
    </defs>
    <rect x="0" y="0" width="345" height="794" fill="var(--teal)"/>
    <polygon points="0,175 175,40 345,150 345,345 0,345" fill="url(#group-tone)" role="img" aria-label="Photo: group of children holding toothbrushes"/>
    <polygon points="430,0 682,0 682,130" fill="var(--teal)"/>
    <polygon points="682,0 1020,0 1020,150 860,202 682,162" fill="var(--teal)"/>
    <polygon points="345,42 373,70 345,98 317,70" fill="var(--slate)"/>
    <polygon points="360,52 382,74 360,96 338,74" fill="var(--slate)" opacity=".55"/>
    <rect x="349" y="449" width="331" height="224" fill="url(#girl-tone)" role="img" aria-label="Photo: smiling girl with glasses and braces"/>
  </svg>

  <div class="block scheme-box">
    <h2 class="heading">Child Dental<br>Benefits Scheme</h2>
    <p class="text">A dental benefits program is available for eligible children aged 2 to 17 and will receive $1000 for dental treatments.</p>
    <p class="text">To check if your children are eligible</p>
    <p class="call">call us on<strong>9400 2186</strong></p>
  </div>

  <div class="block" style="left:477px; top:92px; width:200px;">
    <h2 class="heading heading--teal">Special<br>Promotions</h2>
  </div>
  <div class="block body-copy body-copy--dark" style="left:477px; top:192px; width:200px; font-size:13.5px; line-height:1.35;">
    <p>Gap free dental check-up, clean &amp; x-rays for all health insurances**</p>
    <p>At home whitening kit now <span class="accent">$199</span> limited time only <span class="accent">(normally $395)</span> Braces, dentures and implants are available at our clinic</p>
    <p style="margin-top:26px;">**Conditions apply—Ask staff for more information.</p>
  </div>
  <div class="block address-bar">
    48 Alderbrook Road<br>Westvale, VIC 3999<br>Phone: (03) 9400 2186<br>Email: admin@brindlemoordental.com.au
  </div>

  <div class="block" style="left:818px; top:80px; width:200px;">
    <h2 class="heading heading--white">Dental<br>Providers</h2>
  </div>
  <div class="block providers">
    <div class="provider"><div class="provider__name">Dr Thao Nguyen</div><div class="provider__creds">BDSc (Melb), ICCDE</div></div>
    <div class="provider"><div class="provider__name">Dr Minh Tran</div><div class="provider__creds">BDSc (Melb), FICCDE FRACDS,<br>PGradDipCD Implants (Melb)</div></div>
    <div class="provider"><div class="provider__name">Dr Lan Vo</div><div class="provider__creds">BHsc Mdent (Latrobe)</div></div>
    <div class="provider"><div class="provider__name">Dr Paul Ngo</div><div class="provider__creds">BHsc Mdent (Latrobe), FRACDS</div></div>
    <div class="provider"><div class="provider__name">Dr Kim Ly</div><div class="provider__creds">BDS (Adl)</div></div>
  </div>
  <div class="map" role="img" aria-label="Street map showing the clinic location"
       style="left:713px; top:490px; width:301px; height:259px; background:linear-gradient(135deg,#f6f6f6,#e6e7e8);"></div>
</section>

</body>
</html>
```